Stationery Refresh For Local Mortgage Broker

We want to modernise and standardise our stationery, including: letterhead, presentation folder, email signature and business card.

The new stationery should be a more modern and professional take on our existing colour scheme and brand. (We do not want a complete overhaul.) A folder of approved stock photos can be found here: https://filebox.example-share.net/f/7kQzR2mTn4vWx9Lp3Yb8-HsdJe5Uc1Ga/view

Our current website is: www.brindlecovefin.com.au but we will be updating this to be consistent with our new stationery.

We are open to *very slight* tweaks to our logo if you feel it needs modernising, but overall we would like to maintain consistent colour scheme.

> Letterhead

148 Calloway Parade,
Geelong, VIC, 3220
ABN: 31 805 249 067
Australian Credit License: 718293

(03) 5391 6084
www.brindlecovefin.com.au

> Presentation Folder

148 Calloway Parade,
Geelong, VIC, 3220
(03) 5391 6084
www.brindlecovefin.com.au

ABN: 31 805 249 067

> Email Signature

Liam Tresidder
Director
M. 0412 857 294
P. (03) 5391 6084
www.brindlecovefin.com.au
148 Calloway Parade,
Geelong, VIC, 3220

ABN: 31 805 249 067

(you can also include a photo if you like: https://brindlecovefin.com.au/wp-content/uploads/2020/12/Liam-Tresidder.png.webp)

> Business Card

Liam Tresidder
Director
M. 0412 857 294
P. (03) 5391 6084
www.brindlecovefin.com.au
148 Calloway Parade,
Geelong, VIC, 3220

ABN: 31 805 249 067

Additional information...

If it's useful/relevant, the services we offer are: Home Loans, Investment Loans, Refinance, Debt Consolidation, Commercial Finance, Vehicle Loans
(You may choose to use this in any of the designs)

Target Market(s)

Home Buyers and Investors

Industry/Entity Type

Mortgage broking/property/real estate

Requirements
Must have
• At least somewhat consistent with our current site (yet meaningfully modernized)
Should not have
• dramatically different logo or colourscheme overhauls

```html
<!DOCTYPE html>
<html lang="en">
<head>
<meta charset="utf-8">
<title>Brindlecove Financial Services – Stationery Suite</title>
<link href="https://fonts.googleapis.com/css2?family=Montserrat:wght@400;800&family=Arimo:wght@400&display=swap" rel="stylesheet">
<style>
  :root {
    --backdrop: #6d6e70;
    --paper: #ffffff;
    --brand-red: #9d1b20;
    --ink: #1a1a1a;
    --rule: #8a8a8a;
    --signature-tone: #e9e9e9;
  }
  * { box-sizing: border-box; margin: 0; padding: 0; }
  html, body { width: 1200px; height: 991px; overflow: hidden; }
  body {
    position: relative;
    background: var(--backdrop);
    font-family: "Arimo", Arial, sans-serif;
    color: var(--ink);
  }
  .sheet { position: absolute; background: var(--paper); overflow: hidden; }
  .edge-tab { position: absolute; background: var(--brand-red); }
  .edge-tab--left { left: 0; border-radius: 0 8px 8px 0; }
  .edge-tab--right { right: 0; border-radius: 8px 0 0 8px; }
  .wordmark {
    position: absolute;
    font-family: "Montserrat", sans-serif;
    font-weight: 400;
    color: var(--brand-red);
    white-space: nowrap;
    text-transform: uppercase;
  }

  /* Letterhead */
  .letterhead { left: 187px; top: 154px; width: 394px; height: 509px; }
  .letterhead .edge-tab { top: 68px; width: 12px; height: 373px; }
  .letterhead .wordmark { left: 37px; top: 42px; font-size: 13px; letter-spacing: 5px; }
  .letter-salutation { position: absolute; left: 37px; top: 131px; font-size: 11.5px; }
  .letter-date { position: absolute; right: 32px; top: 131px; font-size: 11.5px; }
  .letter-body {
    position: absolute; left: 59px; top: 178px; width: 273px;
    font-size: 7.4px; line-height: 11.5px; text-align: justify;
  }
  .letter-body p + p { margin-top: 2px; }
  .letter-closing { position: absolute; left: 37px; top: 317px; font-size: 11.5px; }
  .letter-signature {
    position: absolute; left: 31px; top: 335px; width: 86px; height: 118px;
    background: linear-gradient(135deg, var(--signature-tone), #f7f7f7);
  }
  .letter-contact {
    position: absolute; right: 36px; top: 435px;
    font-size: 7.4px; line-height: 9.5px; text-align: right;
  }
  .letter-contact .gap { display: block; height: 9px; }

  /* Presentation folder */
  .folder { left: 609px; top: 124px; width: 404px; height: 539px; }
  .folder .edge-tab { top: 79px; width: 11px; height: 381px; }
  .folder .wordmark {
    left: 0; right: 0; top: 258px; text-align: center;
    font-size: 25px; letter-spacing: 11px; text-indent: 11px;
  }
  .folder-contact {
    position: absolute; left: 0; right: 0; top: 499px; text-align: center;
    font-size: 8px; line-height: 12px; letter-spacing: 1.6px;
  }

  /* Business cards */
  .card { top: 708px; width: 252px; height: 144px; }
  .card--front { left: 59px; background: var(--brand-red); }
  .card--front .edge-tab { background: var(--paper); top: 33px; width: 9px; height: 79px; }
  .card--front .wordmark {
    left: 0; right: 0; top: 64px; text-align: center; color: var(--paper);
    font-size: 15px; letter-spacing: 6px; text-indent: 6px;
  }
  .card--back { left: 339px; }
  .card--back .edge-tab { top: 32px; width: 9px; height: 80px; }
  .card--back .wordmark { left: 14px; width: 110px; top: 65px; text-align: center; font-size: 9px; letter-spacing: 2.4px; }
  .card--back .divider { position: absolute; left: 137px; top: 21px; width: 1px; height: 100px; background: var(--rule); }
  .card-details { position: absolute; left: 154px; top: 22px; font-size: 5.5px; line-height: 7.3px; }
  .person-name { font-family: "Montserrat", sans-serif; font-weight: 800; color: var(--brand-red); }
  .card-details .person-name { font-size: 8.5px; line-height: 10px; }
  .card-details .person-role { font-size: 8px; line-height: 10px; margin-bottom: 10px; }
  .card-details .legal { margin-top: 14px; }

  /* Email signature */
  .email-signature { left: 639px; top: 702px; width: 439px; height: 155px; }
  .email-signature .edge-tab { top: 23px; width: 11px; height: 109px; }
  .email-signature .wordmark { left: 42px; width: 160px; top: 70px; text-align: center; font-size: 12.5px; letter-spacing: 3.4px; }
  .email-signature .divider { position: absolute; left: 230px; top: 27px; width: 1px; height: 105px; background: var(--rule); }
  .signature-details { position: absolute; left: 272px; top: 16px; font-size: 8px; line-height: 9.5px; }
  .signature-details .person-name { font-size: 11.5px; line-height: 14px; }
  .signature-details .person-role { font-size: 10.5px; line-height: 13px; margin-bottom: 10px; }
  .signature-details .legal { margin-top: 11px; }
</style>
</head>
<body>

  <section class="sheet letterhead">
    <span class="edge-tab edge-tab--left"></span>
    <span class="edge-tab edge-tab--right"></span>
    <div class="wordmark">Brindlecove</div>
    <p class="letter-salutation">Dear Customer,</p>
    <p class="letter-date">Aug 10 / 2021</p>
    <div class="letter-body">
      <p>Lorem ipsum dolor sit amet, consectetuer adipiscing elit, sed diam nonummy nibh euismod tincidunt ut laoreet dolore magna aliquam erat volutpat. Ut wisi enim ad minim veniam, quis nostrud exerci tation ullamcorper suscipit lobortis nisl ut aliquip ex ea commodo consequat. Duis autem vel eum iriure dolor in hendrerit in vulputate velit esse molestie consequat, vel illum dolore eu feugiat nulla facilisis at vero eros et accumsan et iusto odio dignissim qui blandit praesent luptatum zzril delenit augue duis dolore te feugait nulla facilisi.</p>
      <p>Lorem ipsum dolor sit amet, cons ectetuer adipiscing elit, sed diam nonummy nibh euismod tincidunt ut laoreet dolore magna aliquam erat volutpat. Ut wisi</p>
    </div>
    <p class="letter-closing">Yours Lovingly,</p>
    <div class="letter-signature" role="img" aria-label="Handwritten signature of the director"></div>
    <address class="letter-contact" style="font-style:normal">
      148 Calloway Parade,<br>
      Geelong, VIC, 3220<br>
      ABN: 31 805 249 067<br>
      Australian Credit License: 718293
      <span class="gap"></span>
      (03) 5391 6084<br>
      www.brindlecovefin.com.au
    </address>
  </section>

  <section class="sheet folder">
    <span class="edge-tab edge-tab--left"></span>
    <span class="edge-tab edge-tab--right"></span>
    <div class="wordmark">Brindlecove</div>
    <p class="folder-contact">
      148 Calloway Parade, Geelong, VIC, 3220 I (03) 5391 6084<br>
      www.brindlecovefin.com.au I ABN: 31 805 249 067<br>
      Australian Credit License: 718293
    </p>
  </section>

  <section class="sheet card card--front">
    <span class="edge-tab edge-tab--left"></span>
    <span class="edge-tab edge-tab--right"></span>
    <div class="wordmark">Brindlecove</div>
  </section>

  <section class="sheet card card--back">
    <span class="edge-tab edge-tab--left"></span>
    <span class="edge-tab edge-tab--right"></span>
    <div class="wordmark">Brindlecove</div>
    <span class="divider"></span>
    <div class="card-details">
      <p class="person-name">Liam Tresidder</p>
      <p class="person-role">Director</p>
      <p>M. 0412 857 294<br>P. (03) 5391 6084<br>www.brindlecovefin.com.au<br>148 Calloway Parade,<br>Geelong, VIC, 3220</p>
      <p class="legal">ABN: 31 805 249 067<br>Australian Credit License: 718293</p>
    </div>
  </section>

  <section class="sheet email-signature">
    <span class="edge-tab edge-tab--left"></span>
    <span class="edge-tab edge-tab--right"></span>
    <div class="wordmark">Brindlecove</div>
    <span class="divider"></span>
    <div class="signature-details">
      <p class="person-name">Liam Tresidder</p>
      <p class="person-role">Director</p>
      <p>M. 0412 857 294<br>P. (03) 5391 6084<br>www.brindlecovefin.com.au<br>148 Calloway Parade,<br>Geelong, VIC, 3220</p>
      <p class="legal">ABN: 31 805 249 067<br>Australian Credit License: 718293</p>
    </div>
  </section>

</body>
</html>
```